Boutique Barre Studio in Geneva

Business card for pilates and dance studio. We are a brand new studio and love our fresh image with our yellow color. This business card is meant for our founder.

```html
<!DOCTYPE html>
<html lang="en">
<head>
<meta charset="utf-8">
<title>linea studio – business card</title>
<link href="https://fonts.googleapis.com/css2?family=Open+Sans:wght@300;400&display=swap" rel="stylesheet">
<style>
  :root {
    --bg: #2a2a2a;
    --yellow: #e3d77a;
    --yellow-deep: #ddd072;
    --white: #f7f7f5;
    --ink: #3b3b38;
    --ink-soft: #5e5c4c;
    --salmon: #c98a72;
    --sky: #a6c8ea;
  }
  * { margin: 0; padding: 0; box-sizing: border-box; }
  html, body { width: 1200px; height: 1138px; overflow: hidden; background: var(--bg); }
  body { position: relative; font-family: 'Open Sans', sans-serif; }

  .card {
    position: absolute;
    left: 289px;
    width: 622px;
    height: 376px;
    border-radius: 18px;
    background: var(--yellow);
    overflow: hidden;
  }
  .card--front { top: 186px; }
  .card--back { top: 608px; }

  /* front */
  .brand {
    position: absolute;
    left: 0; right: 0;
    text-align: center;
    color: var(--white);
    font-weight: 300;
    line-height: 1;
  }
  .card--front .brand { top: 88px; }
  .brand__word { display: block; font-size: 104px; letter-spacing: 2px; }
  .brand__sub { display: block; font-size: 26px; letter-spacing: 4px; margin-top: 4px; }

  .services {
    position: absolute;
    left: 0; top: 298px;
    width: 100%; height: 32px;
    background: linear-gradient(90deg, var(--salmon) 0%, #d9b7a4 45%, var(--sky) 100%);
    color: var(--white);
    font-size: 16px;
    font-weight: 300;
    letter-spacing: 1.5px;
    text-align: center;
    line-height: 32px;
  }
  .front-footer {
    position: absolute;
    left: 0; right: 0; top: 338px;
    text-align: center;
    font-size: 15px;
    color: var(--ink-soft);
    display: flex;
    justify-content: center;
    align-items: center;
    gap: 12px;
  }
  .social-dot {
    width: 10px; height: 10px; border-radius: 50%;
    background: var(--salmon);
    display: inline-block;
  }

  /* back */
  .card--back .blob { position: absolute; left: 0; top: 0; }
  .card--back .brand { left: 300px; right: 0; top: 92px; color: var(--yellow-deep); }
  .card--back .brand__word { font-size: 72px; }
  .card--back .brand__sub { font-size: 18px; letter-spacing: 3px; }

  .person { position: absolute; left: 30px; top: 64px; color: var(--ink); }
  .person__name { font-size: 25px; font-weight: 400; }
  .person__role { font-size: 15px; color: var(--ink-soft); margin-top: 2px; }

  .contacts {
    position: absolute; left: 30px; top: 244px;
    list-style: none;
    font-size: 16px;
    color: var(--ink-soft);
  }
  .contacts li { display: flex; align-items: center; height: 25px; }
  .contacts svg { width: 16px; height: 16px; margin-right: 16px; }
  .contacts .address { margin-top: 6px; }
</style>
</head>
<body>

<section class="card card--front">
  <div class="brand">
    <span class="brand__word">linea</span>
    <span class="brand__sub">STUDIO</span>
  </div>
  <div class="services">BARRE | PILATES | REFORMER | YOGA | DANCE</div>
  <div class="front-footer">
    <span>www.linea-studio.com</span>
    <span class="social-dot"></span>
    <span>@lineastudiogeneva</span>
  </div>
</section>

<section class="card card--back">
  <svg class="blob" width="622" height="376" viewBox="0 0 622 376">
    <path d="M296,0 C262,70 254,190 296,236 C338,280 430,288 622,282 L622,0 Z" fill="#a6c8ea"/>
    <path d="M304,0 C272,70 264,186 304,230 C346,274 440,282 622,278 L622,0 Z" fill="#f7f7f5"/>
  </svg>
  <div class="brand">
    <span class="brand__word">linea</span>
    <span class="brand__sub">STUDIO</span>
  </div>

  <div class="person">
    <div class="person__name">Mara Lindqvist</div>
    <div class="person__role">Founder LS</div>
  </div>

  <ul class="contacts">
    <li>
      <svg viewBox="0 0 16 16" fill="none" stroke="#3b3b38" stroke-width="1.2"><circle cx="8" cy="8" r="7"/><path d="M5.5 4.5l1.2 1.8-.8 1c.5 1 1.3 1.8 2.3 2.3l1-.8 1.8 1.2-.6 1.2c-2.8-.4-5-2.6-5.4-5.4z"/></svg>
      +33 612450378
    </li>
    <li>
      <svg viewBox="0 0 16 16" fill="none" stroke="#3b3b38" stroke-width="1.2"><rect x="1" y="3" width="14" height="10"/><path d="M1 3l7 6 7-6"/></svg>
      hello@linea-studio.com
    </li>
    <li>
      <svg viewBox="0 0 16 16" fill="none" stroke="#3b3b38" stroke-width="1.2"><circle cx="8" cy="8" r="7"/><ellipse cx="8" cy="8" rx="3" ry="7"/><path d="M1 8h14M2.5 4.5h11M2.5 11.5h11"/></svg>
      www.linea-studio.com
    </li>
    <li class="address">Rue des Lilas 12 1205 Geneva, Switzerland</li>
  </ul>
</section>

</body>
</html>
```